Psychotherapist need a business card with logo

I am a psychotherapist in need of a business card. The card must have:

Marisol Trevuneda
Psicoterapeuta
937 281 706

CLAROVIA use the greek letter psy, which is the psychologist symbol, but I would prefer something like a mandala, a graphic symbol, an iconic tree, nothing very usual, but something that shows confidence and trust.

Industry/Entity Type

Business

```html
<!DOCTYPE html>
<html lang="es">
<head>
<meta charset="utf-8">
<title>Marisol Trevuneda – Business Card</title>
<link rel="stylesheet" href="https://fonts.googleapis.com/css2?family=Source+Sans+3:wght@300;400;700&display=swap">
<style>
  :root {
    --stage: #1f6a3a;
    --card: #ffffff;
    --ink-strong: #666666;
    --ink-soft: #777777;
    --accent-gold: #f2c24a;
    --mark-tint: #cfe6c9;
    --wave-mist: #eef1ec;
    --wave-green: #cfe3c6;
    --wave-cream: #eef0d8;
  }
  html, body {
    margin: 0;
    padding: 0;
    width: 1200px;
    height: 1000px;
    overflow: hidden;
    background: var(--stage);
    font-family: "Source Sans 3", "Myriad Pro", Arial, sans-serif;
  }
  .business-card {
    position: absolute;
    left: 278px;
    top: 298px;
    width: 644px;
    height: 368px;
    background: var(--card);
    overflow: hidden;
  }
  .wave-area {
    position: absolute;
    left: 0;
    top: 210px;
    width: 644px;
    height: 158px;
    background: linear-gradient(to bottom,
      rgba(255,255,255,0) 0%,
      var(--wave-mist) 45%,
      var(--wave-green) 80%,
      var(--wave-cream) 100%);
  }
  .brand-mark {
    position: absolute;
    left: 270px;
    top: 46px;
    width: 104px;
    height: 104px;
    border-radius: 50%;
    background: var(--mark-tint);
  }
  .brand-name {
    position: absolute;
    left: 0;
    top: 170px;
    width: 644px;
    text-align: center;
    font-weight: 700;
    font-size: 24px;
    line-height: 30px;
    letter-spacing: 0.3px;
    color: var(--ink-strong);
  }
  .person {
    position: absolute;
    left: 0;
    top: 232px;
    width: 311px;
    text-align: right;
  }
  .divider {
    position: absolute;
    left: 321px;
    top: 232px;
    width: 2px;
    height: 44px;
    background: var(--accent-gold);
  }
  .reach {
    position: absolute;
    left: 337px;
    top: 232px;
    width: 290px;
  }
  .person-name, .phone {
    font-size: 19px;
    font-weight: 400;
    color: var(--ink-soft);
    line-height: 24px;
  }
  .person-role, .email {
    font-size: 16px;
    font-weight: 400;
    color: var(--ink-soft);
    line-height: 22px;
  }
</style>
</head>
<body>
  <section class="business-card">
    <div class="wave-area" role="img" aria-label="Soft flowing white and green wave decoration along the bottom edge"></div>

    <div class="brand-mark"></div>
    <div class="brand-name">CLAROVIA</div>

    <div class="person">
      <div class="person-name">Marisol Trevuneda</div>
      <div class="person-role">Psicoterapeuta</div>
    </div>
    <div class="divider"></div>
    <div class="reach">
      <div class="phone">937 281 706</div>
      <div class="email">info@clarovia.com</div>
    </div>
  </section>
</body>
</html>
```